500ml Aluminium drinking Water Bottle. Endlessly reusable and refillable

We need a label for our new 500ml water bottle. We are Sip Carrowbeg based in the Scottish Highlands. We extract filter and bottle drinking water from Loch Ness in Scotland. We currently have on the market a 100ml bottle of water designed for whisky drinkers see - www.384aquafine.com
We now want to create a 500ml bottle of still and sparkling water using aluminium bottles which allows us much more room for branding. Our water will be exclusive and high end, not available in the supermarkets only selected outlets. Our current branding is based on the the number 384 which relates to the depth of the Loch at 384 Fathoms. We have interwound the legendary loch ness monster into the top half of the numbers. We will use the 384 logo on our new 500ml product but need a creative approach as to how it is presented on the bottle. Our 100ml Drops for Brandy" product will stand alone, our new 500ml will use the same 384 logo, but its strap line will be changed to differentiate between our products. We need to maximise the available space on the aluminium bottle to ensure our product leaps out at the consumer. The available space for the new branding is 207mm wide x 120mm high, but in this space we need allow room for our barcode, address and statutory information, but we can scale these up or down. Our new design will be exclusive and elegant, not loud or harsh. It will represent a unique drinking water product from an iconic water source. So the branding of 384 is supplied. Our target consumer is middle aged and above with a disposable income,, those who want to experience rare and exclusive products and who are prepared to pay for that luxury.

Hi Guys - please fee free to use the 384 logo, but leave out "Drops for Brandy". We are trying to create a label for 500ml aluminium bottles of still and sparkling drinking water for any occasion. We need the label design to be bold and vibrant but not brash or harsh. We are targeting exclusive retail and high end dining outlets, where the consumer will appreciate the pure water from the Scottish highlands. The history and scenery of Scotland should provide some inspiration for your designs or colour palette. We want to invoke thoughts of cold clear water and the refreshing taste of our pure water.

Target Market(s)

Exclusive high end consumers

Industry/Entity Type

food and drink

Requirements
Must have
• clear bright color scheme clever positioning of the logo
Should not have
• the term "Loch Ness Water" must not appear

```html
<!DOCTYPE html>
<html lang="en">
<head>
<meta charset="utf-8">
<title>384 Pure Water – 500ml Label</title>
<link rel="stylesheet" href="https://fonts.googleapis.com/css2?family=Oswald:wght@200;300;400&family=Nunito+Sans:wght@400&display=swap">
<style>
  :root {
    --page: #ffffff;
    --mist: #d4ecf9;
    --sky: #00b8ee;
    --deep-blue: #0a6fc0;
    --loch-teal: #1a5a60;
    --scene-top: #12a6e4;
    --scene-hill: #86b55e;
    --scene-water: #5d8591;
    --label-white: #ffffff;
    --tab-text: #dbeefc;
  }
  html, body {
    margin: 0;
    padding: 0;
    width: 927px;
    height: 1200px;
    overflow: hidden;
    background: var(--page);
  }
  .label {
    display: block;
    width: 927px;
    height: 1200px;
  }
  .label__mist { fill: var(--mist); }
  .label__band { fill: var(--sky); }
  .label__drop-frame { fill: var(--deep-blue); }
  .label__tab { fill: var(--deep-blue); }
  .brand-name {
    font-family: "Oswald", sans-serif;
    font-weight: 400;
    fill: var(--loch-teal);
  }
  .product-title {
    font-family: "Oswald", sans-serif;
    font-weight: 200;
    fill: var(--label-white);
  }
  .volume {
    font-family: "Nunito Sans", sans-serif;
    font-weight: 400;
    fill: var(--tab-text);
  }
</style>
</head>
<body>
<svg class="label" viewBox="445 790 780 1010" preserveAspectRatio="xMidYMid meet" xmlns="http://www.w3.org/2000/svg">
  <defs>
    <linearGradient id="scene-tones" x1="0" y1="0" x2="0" y2="1">
      <stop offset="0" stop-color="var(--sky)"/>
      <stop offset="0.3" stop-color="var(--scene-top)"/>
      <stop offset="0.55" stop-color="var(--scene-hill)"/>
      <stop offset="0.8" stop-color="var(--scene-water)"/>
      <stop offset="1" stop-color="var(--scene-water)"/>
    </linearGradient>
  </defs>

  <!-- drop-shaped frame -->
  <path class="label__drop-frame" d="M700 1345 L990 1345 L1038 1420 A235 235 0 1 1 632 1420 Z"/>
  <path class="label__scene" role="img" aria-label="Scottish highland glen with green mountains and a clear rocky river under a blue sky"
        fill="url(#scene-tones)"
        d="M712 1355 L980 1355 L1024 1424 A220 220 0 1 1 646 1424 Z"/>

  <!-- logo panel -->
  <rect class="label__mist" x="680" y="828" width="312" height="255"/>
  <text class="brand-name" x="835" y="1025" text-anchor="middle" font-size="150">384</text>

  <!-- title band -->
  <rect class="label__band" x="680" y="1083" width="312" height="277"/>
  <text class="product-title" x="835" y="1195" text-anchor="middle" font-size="118" textLength="182" lengthAdjust="spacingAndGlyphs">PURE</text>
  <text class="product-title" x="836" y="1316" text-anchor="middle" font-size="118" textLength="262" lengthAdjust="spacingAndGlyphs">WATER</text>

  <!-- volume tab -->
  <path class="label__tab" d="M770 1765 Q775 1700 835 1698 Q895 1700 905 1760 Z"/>
  <text class="volume" x="835" y="1732" text-anchor="middle" font-size="23">500ml</text>
</svg>
</body>
</html>
```